K7 Digital Stationery Design Project

We are looking to have stationary designs created for our company branding materials. We are looking for the following to be created.
1. Business Cards (front & back)
2. Letterhead
3. Envelopes #10
We are a new Strategy, Build and Growth Studio firm. Primary color scheme is desired to be blue/grey/white. This web start-up is owned and operated by individuals with 15+ years experience each in the industry so should not look as though it is a start-up by young/inexperienced individuals.
We build website & custom applications/software. In addition we provide the full spectrum of web marketing solutions including SEO, PPC, Social Media, Branding, Content Marketing and PR.
Please let us know if you have any questions. Looking forward to seeing all the amazing design ideas.
Attached is our logo.
Thanks!
Target Market(s)
Company will be nearly 100% business to business sales. Looking to work with companies that are already established, with a website, who want to take their website and/or online marketing efforts to the next level.
Industry/Entity Type
Marketing
Look and feel

```html
<!DOCTYPE html>
<html lang="en">
<head>
<meta charset="utf-8">
<title>K7 Digital Stationery</title>
<link href="https://fonts.googleapis.com/css2?family=Arimo:wght@400;700&display=swap" rel="stylesheet">
<style>
  :root {
    --bg: #e4e4e4;
    --paper: #ffffff;
    --blue: #1a7cc4;
    --blue-light: #2aa3dc;
    --blue-faint: #e8eef6;
    --ink: #222222;
    --ink-soft: #555555;
  }
  * { margin: 0; padding: 0; box-sizing: border-box; }
  html, body { width: 1200px; height: 800px; overflow: hidden; }
  body { background: var(--bg); font-family: "Arimo", Arial, sans-serif; color: var(--ink); position: relative; }

  .sheet { position: absolute; background: var(--paper); overflow: hidden; }
  .brand-block { position: absolute; background: linear-gradient(180deg, var(--blue-light), var(--blue)); }
  .base-bar { position: absolute; left: 0; right: 0; bottom: 0; background: var(--blue); }
  .faint-disc { position: absolute; border-radius: 50%; background: var(--blue-faint); }

  .brand { position: absolute; color: var(--blue); }
  .brand-name { font-weight: 700; letter-spacing: 0.3px; white-space: nowrap; display: flex; align-items: center; gap: 4px; }
  .brand-dot { display: inline-block; border-radius: 50%; background: var(--blue); }
  .brand-tagline { color: var(--ink-soft); white-space: nowrap; }

  .contact { position: absolute; color: var(--ink); line-height: 1.2; font-style: normal; }
  .contact .label { color: var(--blue-light); }

  .web { position: absolute; color: var(--ink); white-space: nowrap; }
  .web b { font-weight: 700; }

  /* Letterhead */
  .letterhead { left: 261px; top: 192px; width: 307px; height: 433px; }
  .letterhead .brand-block { left: 0; top: 12px; width: 32px; height: 60px; }
  .letterhead .brand { left: 42px; top: 56px; }
  .letterhead .brand-name { font-size: 10.5px; }
  .letterhead .brand-dot { width: 6px; height: 6px; }
  .letterhead .brand-tagline { font-size: 4px; margin-top: 1px; }
  .letterhead .contact { left: 132px; top: 24px; font-size: 6.3px; }
  .letterhead .contact .gap { height: 4px; }
  .letterhead .faint-disc { left: 200px; top: 225px; width: 150px; height: 150px; }
  .letter-body { position: absolute; left: 33px; top: 90px; width: 258px; font-size: 5.1px; line-height: 7.9px; color: var(--ink); }
  .letter-body p { text-align: justify; margin-bottom: 7px; }
  .letter-body .greeting { margin-bottom: 5px; }
  .signature { width: 90px; height: 20px; margin: 4px 0 2px; background: linear-gradient(90deg, #f4f4f4, #ececec); }
  .signer { margin-left: 46px; line-height: 6.5px; }
  .letterhead .web { right: 24px; bottom: 17px; font-size: 8px; }
  .letterhead .base-bar { height: 12px; }

  /* Business card front */
  .card-front { left: 598px; top: 303px; width: 132px; height: 76px; }
  .card-pattern { position: absolute; inset: 0; background: linear-gradient(135deg, var(--blue-light), var(--blue)); }
  .card-front .brand { left: 0; right: 0; top: 44px; display: flex; flex-direction: column; align-items: center; color: #fff; }
  .card-front .brand-name { font-size: 7.5px; }
  .card-front .brand-dot { width: 4px; height: 4px; background: #fff; }
  .card-front .brand-tagline { font-size: 3px; color: #e6f3fb; }
  .card-front .web { left: 0; right: 0; bottom: 7px; text-align: center; font-size: 3.6px; color: #fff; }

  /* Business card back */
  .card-back { left: 786px; top: 302px; width: 131px; height: 76px; }
  .card-back .brand-block { left: 0; top: 24px; width: 11px; height: 27px; }
  .card-back .faint-disc { left: 22px; top: 46px; width: 30px; height: 30px; }
  .card-back .brand { left: 15px; top: 47px; }
  .card-back .brand-name { font-size: 5px; gap: 2px; }
  .card-back .brand-dot { width: 3px; height: 3px; }
  .card-back .brand-tagline { font-size: 2px; }
  .card-holder { position: absolute; left: 62px; top: 22px; font-size: 2.6px; line-height: 3.4px; color: var(--ink-soft); }
  .card-holder .name { font-size: 4.2px; color: var(--ink); line-height: 5px; }
  .card-holder .role { font-size: 2.8px; color: var(--ink-soft); }
  .card-holder .gap { height: 2px; }
  .card-back .web { left: 62px; top: 51px; font-size: 3.2px; }
  .card-back .base-bar { height: 4px; }

  /* Envelope */
  .envelope { left: 593px; top: 402px; width: 332px; height: 154px; }
  .envelope .brand-block { left: 0; top: 8px; width: 22px; height: 58px; }
  .envelope .faint-disc { left: 28px; top: 40px; width: 92px; height: 92px; }
  .envelope .brand { left: 32px; top: 54px; }
  .envelope .brand-name { font-size: 9px; }
  .envelope .brand-dot { width: 5px; height: 5px; }
  .envelope .brand-tagline { font-size: 3.5px; }
  .envelope .contact { left: 117px; top: 22px; font-size: 6.3px; }
  .envelope .contact .gap { height: 4px; }
  .envelope .web { left: 4px; top: 136px; font-size: 7.5px; }
  .envelope .base-bar { height: 6px; }
</style>
</head>
<body>

  <section class="sheet letterhead" aria-label="Letterhead">
    <div class="brand-block"></div>
    <div class="faint-disc"></div>
    <div class="brand">
      <div class="brand-name"><span class="brand-dot"></span>K7 DIGITAL</div>
      <div class="brand-tagline">Strategy, Build and Growth Studio</div>
    </div>
    <address class="contact">
      0 Harbor Point Drive, Suite 00000,<br>Millbrook, NC 00000
      <div class="gap"></div>
      <span class="label">P:</span> +1 000 555 0142<br>
      <span class="label">F:</span> +1 000 555 0143<br>
      <span class="label">E:</span> office@k7digital.com
    </address>
    <div class="letter-body">
      <p class="greeting">Dear Client,</p>
      <p>Lorem ipsum dolor sit amet, consectetur adipisicing elit, sed do eiusmod tempor incididunt ut labore et dolore magna aliqua. Ut enim ad minim veniam, quis nostrud exercitation ullamco laboris nisi ut aliquip ex ea commodo consequat. Duis aute irure dolor in reprehenderit in voluptate velit esse cillum dolore eu fugiat nulla pariatur. Excepteur sint occaecat cupidatat non proident, sunt in culpa qui officia deserunt mollit anim id est laborum.</p>
      <p>Lorem ipsum dolor sit amet, consectetur adipisicing elit, sed do eiusmod tempor incididunt ut labore et dolore magna aliqua. Ut enim ad minim veniam, quis nostrud exercitation ullamco laboris nisi ut aliquip ex ea commodo consequat. Duis aute irure dolor in reprehenderit in voluptate velit esse cillum dolore eu fugiat nulla pariatur. Excepteur sint occaecat cupidatat non proident, sunt in culpa qui officia deserunt mollit anim id est laborum.</p>
      <p>Lorem ipsum dolor sit amet, consectetur adipisicing elit, sed do eiusmod tempor incididunt ut labore et dolore magna aliqua. Ut enim ad minim veniam, quis nostrud exercitation ullamco laboris nisi ut aliquip ex ea commodo consequat. Duis aute irure dolor in reprehenderit in voluptate velit esse cillum dolore eu fugiat nulla pariatur. Excepteur sint occaecat cupidatat non proident, sunt in culpa qui officia deserunt mollit anim id est laborum.</p>
      <p>Lorem ipsum dolor sit amet, consectetur adipisicing elit, sed do eiusmod tempor incididunt ut labore et dolore magna aliqua. Ut enim ad minim veniam, quis nostrud exercitation ullamco laboris nisi ut aliquip ex ea commodo consequat. Duis aute irure dolor in reprehenderit in voluptate velit esse cillum dolore eu fugiat nulla pariatur. Excepteur sint occaecat cupidatat non proident, sunt in culpa qui officia deserunt mollit anim id est laborum.</p>
      <p>Lorem ipsum dolor sit amet, consectetur adipisicing elit, sed do eiusmod tempor incididunt ut labore et dolore magna aliqua. Ut enim ad minim veniam, quis nostrud exercitation ullamco laboris nisi ut aliquip ex ea commodo consequat. Duis aute irure dolor in reprehenderit in voluptate velit esse cillum dolore eu fugiat nulla pariatur. Excepteur sint occaecat cupidatat non proident, sunt in culpa qui officia deserunt mollit anim id est laborum.</p>
      <div>Yours Sincerely,</div>
      <div class="signature" role="img" aria-label="Handwritten signature of Paul Warner"></div>
      <div class="signer">Paul Warner<br>Executive manager</div>
    </div>
    <div class="web">www.<b>k7digital</b>.com</div>
    <div class="base-bar"></div>
  </section>

  <section class="sheet card-front" aria-label="Business card front">
    <div class="card-pattern" role="img" aria-label="Repeating blue brand pattern background"></div>
    <div class="brand">
      <div class="brand-name"><span class="brand-dot"></span>K7 DIGITAL</div>
      <div class="brand-tagline">Strategy, Build and Growth Studio</div>
    </div>
    <div class="web">www.k7digital.com</div>
  </section>

  <section class="sheet card-back" aria-label="Business card back">
    <div class="brand-block"></div>
    <div class="faint-disc"></div>
    <div class="brand">
      <div class="brand-name"><span class="brand-dot"></span>K7 DIGITAL</div>
      <div class="brand-tagline">Strategy, Build and Growth Studio</div>
    </div>
    <div class="card-holder">
      <div class="name">Mark Ellison <span class="role">Manager</span></div>
      0 Harbor Point Drive, Suite 00000,<br>Millbrook, NC 00000
      <div class="gap"></div>
      T: +1 000 555 0144<br>
      F: +1 000 555 0143<br>
      E: mark@k7digital.com
    </div>
    <div class="web">www.k7digital.com</div>
    <div class="base-bar"></div>
  </section>

  <section class="sheet envelope" aria-label="Envelope #10">
    <div class="brand-block"></div>
    <div class="faint-disc"></div>
    <div class="brand">
      <div class="brand-name"><span class="brand-dot"></span>K7 DIGITAL</div>
      <div class="brand-tagline">Strategy, Build and Growth Studio</div>
    </div>
    <address class="contact">
      0 Harbor Point Drive, Suite 00000,<br>Millbrook, NC 00000
      <div class="gap"></div>
      <span class="label">P:</span> +1 000 555 0142<br>
      <span class="label">F:</span> +1 000 555 0143<br>
      <span class="label">E:</span> office@k7digital.com
    </address>
    <div class="web">www.<b>k7digital</b>.com</div>
    <div class="base-bar"></div>
  </section>

</body>
</html>
```